QM Studios needs and Interior Design Business card

I can do anything from Commercial to Residential and Free lance. Beginning to end in design selection process.
Need something to catch the eye of potential customers and vendors. From furniture to Tile and Cabinet selections. I can do it all.

Industry/Entity Type

Design Agency

Contact Information for Business Card

QM Studios- Design Consultanting Residential, Commerical
Maybe a cool detail background. Wall paper print that can have some texture

Font styles to use
Serif

Colors
709dcb
34a6d7
b868aa
e667a6
f59296
85acd3
ffffff
000000
5c5c5c

Requirements
Must have
• Square or Rectangular with Rounded edges
• Name
• Address
• Phone
• Email
Nice to have
• Some colored edges More simples not too busy
• Pattern detail in background.
Should not have
• Not too much color

```html
<!DOCTYPE html>
<html lang="en">
<head>
<meta charset="utf-8">
<title>QM Studios – Business Card</title>
<link rel="stylesheet" href="https://fonts.googleapis.com/css2?family=Didact+Gothic&family=Roboto:wght@400;500&display=swap">
<style>
  :root {
    --ink: #000000;
    --paper: #ffffff;
    --sky: #34a6d7;
    --steel: #709dcb;
    --mist: #85acd3;
    --mist-light: #a9c6e4;
    --grey: #5c5c5c;
    --stage: #e8e5e0;
  }
  * { box-sizing: border-box; margin: 0; padding: 0; }
  html, body { width: 1200px; height: 892px; overflow: hidden; }
  body {
    background: var(--stage);
    display: flex;
    flex-direction: column;
    align-items: center;
    justify-content: center;
    gap: 44px;
    font-family: "Roboto", Arial, sans-serif;
  }
  .card {
    position: relative;
    width: 560px;
    height: 320px;
    border-radius: 12px;
    overflow: hidden;
    box-shadow: 0 6px 18px rgba(0,0,0,.18);
  }

  /* Front */
  .card--front { background: var(--ink); color: var(--paper); }
  .front__band {
    position: absolute; left: 0; right: 0; bottom: 0; height: 40px;
    background: var(--steel);
  }
  .front__rule {
    position: absolute; left: 0; right: 0; bottom: 46px; height: 2px;
    background: var(--sky);
  }
  .front__brand {
    position: absolute; left: 0; top: 0; width: 270px; height: 274px;
    display: flex; align-items: center; justify-content: center; gap: 14px;
  }
  .brand__dot {
    width: 34px; height: 34px; border: 3px solid var(--paper); border-radius: 50%;
    flex: none;
  }
  .brand__name {
    font-family: "Didact Gothic", "Century Gothic", sans-serif;
    font-size: 30px; letter-spacing: 6px; color: var(--paper);
    white-space: nowrap;
  }
  .front__divider {
    position: absolute; left: 276px; top: 48px; width: 1px; height: 180px;
    background: var(--paper); opacity: .85;
  }
  .front__contact {
    position: absolute; left: 306px; top: 58px;
  }
  .contact__name { font-size: 29px; font-weight: 500; color: var(--sky); line-height: 1.05; }
  .contact__title { font-size: 19px; font-weight: 500; color: var(--paper); margin-bottom: 30px; }
  .contact__line {
    display: flex; align-items: center; gap: 10px;
    font-size: 16px; color: var(--paper); margin-bottom: 10px;
  }
  .contact__icon { width: 14px; height: 14px; flex: none; }

  /* Back */
  .card--back {
    background: linear-gradient(160deg, var(--mist-light) 0%, var(--mist) 55%, var(--steel) 100%);
  }
  .back__edge {
    position: absolute; left: 0; right: 0; top: 0; height: 30px; background: var(--ink);
  }
  .back__rule {
    position: absolute; left: 0; right: 0; top: 36px; height: 2px; background: var(--ink);
  }
  .back__name {
    position: absolute; left: 32px; top: 52px;
    font-family: "Didact Gothic", "Century Gothic", sans-serif;
    font-size: 52px; letter-spacing: 12px; color: var(--ink);
  }
  .back__services {
    position: absolute; left: 40px; top: 148px; list-style: none;
    font-size: 19px; color: var(--paper); line-height: 1.5;
  }
  .back__services li::before {
    content: ""; display: inline-block; width: 6px; height: 6px; border-radius: 50%;
    background: var(--paper); margin-right: 12px; vertical-align: middle;
  }
</style>
</head>
<body>
  <section class="card card--front" aria-label="Business card front">
    <div class="front__brand">
      <span class="brand__dot"></span>
      <span class="brand__name">QM Studios</span>
    </div>
    <div class="front__divider"></div>
    <div class="front__contact">
      <p class="contact__name">Nora Vellacott</p>
      <p class="contact__title">Design Consultant</p>
      <p class="contact__line">
        <svg class="contact__icon" viewBox="0 0 14 14" aria-hidden="true">
          <rect width="14" height="14" fill="#34a6d7"/>
          <path d="M4 3.5 L5.8 3.5 L6.4 5.4 L5.4 6.2 Q6.2 7.9 7.8 8.6 L8.6 7.6 L10.5 8.2 L10.5 10 Q5.5 10.4 4 3.5Z" fill="#000"/>
        </svg>
        021 5550 1842
      </p>
      <p class="contact__line">
        <svg class="contact__icon" viewBox="0 0 14 14" aria-hidden="true">
          <rect width="14" height="14" fill="#34a6d7"/>
          <rect x="3" y="4" width="8" height="6" fill="none" stroke="#000" stroke-width="1"/>
          <path d="M3 4 L7 7.5 L11 4" fill="none" stroke="#000" stroke-width="1"/>
        </svg>
        qmstudios@mail.com
      </p>
    </div>
    <div class="front__rule"></div>
    <div class="front__band"></div>
  </section>

  <section class="card card--back" aria-label="Business card back">
    <div class="back__edge"></div>
    <div class="back__rule"></div>
    <p class="back__name">QM Studios</p>
    <ul class="back__services">
      <li>Interior Selections</li>
      <li>flooring</li>
      <li>cabinetry</li>
      <li>paint colors etc.</li>
    </ul>
  </section>
</body>
</html>
```